law firm business cards

I need a business card using my existing logo. Two sided is best because there is a lot of information that needs to go on the card. Use the same general color scheme as logo, but I need one set with the blue background of my website (www.kestonlegalgroup.com), and one set with white background (to see which one I like best).

Information that must be on there:
Darren P. Holloway
Board Certified Civil Trial Specialist
738 Brindlewood Ave., Suite 2300
Raleigh, NC 27699

T 919-555-0142
F 919-555-0187

www.kestonlegalgroup.com
darren@kestonlegalgroup.com

Personal Injury | Criminal Law (to separate the two, pls use a bullet point or pipeline symbol "|"

If there is a way to work in the QRVC logo (maybe at the bottom somewhere), put it in, but don't let it detract from the main logo too much.

Also, if there is a way to work it in, put in somewhere: Former Insurance Company Attorney | Former Criminal Prosecutor (to separate the two, pls use a bullet point or pipeline symbol "|"

```html
<!DOCTYPE html>
<html lang="en">
<head>
<meta charset="utf-8">
<title>Keston Legal — Business Cards</title>
<link href="https://fonts.googleapis.com/css2?family=Cinzel:wght@400;600&family=Open+Sans:wght@400;600;700&display=swap" rel="stylesheet">
<style>
  :root {
    --navy: #213a6b;
    --sky: #7fa3d6;
    --mist: #e4e6ea;
    --red: #d3263b;
    --white: #ffffff;
    --stage: #3d312a;
  }
  * { box-sizing: border-box; margin: 0; padding: 0; }
  html, body { width: 1200px; height: 469px; overflow: hidden; }
  body { background: var(--stage); position: relative; font-family: "Open Sans", Arial, sans-serif; }

  .card {
    position: absolute;
    top: 102px;
    width: 468px;
    height: 264px;
    overflow: hidden;
  }
  .card--front { left: 106px; background: var(--white); }
  .card--back { left: 606px; background: var(--navy); }

  .card__accent-band {
    position: absolute;
    left: 0; right: 0; bottom: 0;
    height: 118px;
    background: linear-gradient(180deg, var(--white) 0%, var(--mist) 10%, var(--sky) 24%, var(--navy) 40%, var(--navy) 100%);
  }

  .firm-mark {
    position: absolute;
    left: 0; right: 0;
    display: flex;
    align-items: center;
    justify-content: center;
    gap: 12px;
    font-family: "Cinzel", Georgia, serif;
    font-weight: 600;
    font-size: 33px;
    letter-spacing: 0.5px;
    line-height: 1;
  }
  .firm-mark__dot { width: 28px; height: 28px; border-radius: 50%; flex: none; }
  .card--front .firm-mark { top: 28px; color: var(--navy); }
  .card--front .firm-mark__dot { background: var(--navy); }
  .card--back .firm-mark { top: 76px; color: var(--white); }
  .card--back .firm-mark__dot { background: var(--white); }

  .attorney-name {
    position: absolute;
    top: 100px; left: 0; right: 0;
    text-align: center;
    font-family: "Cinzel", Georgia, serif;
    font-weight: 600;
    font-size: 19px;
    color: var(--navy);
    letter-spacing: 0.5px;
  }

  .contact {
    position: absolute;
    top: 204px;
    color: var(--white);
    font-size: 10.5px;
    line-height: 15.5px;
    white-space: nowrap;
  }
  .contact--address { left: 32px; }
  .contact--lines { left: 264px; }
  .contact__label { color: var(--red); font-weight: 600; }
  .contact__web { font-weight: 700; letter-spacing: 1.2px; font-size: 11px; }
  .contact__divider {
    position: absolute;
    left: 236px; top: 206px;
    width: 1px; height: 52px;
    background: var(--red);
  }

  .practice-areas, .credentials {
    position: absolute;
    left: 0; right: 0;
    text-align: center;
    color: var(--white);
    white-space: nowrap;
  }
  .practice-areas {
    top: 208px;
    font-family: "Cinzel", Georgia, serif;
    font-size: 15px;
    letter-spacing: 0.4px;
  }
  .credentials {
    top: 236px;
    font-size: 11px;
    letter-spacing: 0.5px;
  }
  .sep { color: var(--red); padding: 0 8px; }
</style>
</head>
<body>

  <section class="card card--front" aria-label="Business card, white side">
    <div class="card__accent-band" role="img" aria-label="Decorative curved swoosh in grey, light blue and navy"></div>

    <div class="firm-mark"><span class="firm-mark__dot"></span><span>Keston Legal</span></div>
    <h1 class="attorney-name">Darren P. Holloway</h1>

    <div class="contact contact--address">
      <p>Board Certified Civil Trial Specialist</p>
      <p>738 Brindlewood Ave., Suite 2300</p>
      <p>Raleigh, NC 27699</p>
    </div>
    <span class="contact__divider"></span>
    <div class="contact contact--lines">
      <p><span class="contact__label">T:</span> 919-555-0142, &nbsp;<span class="contact__label">F:</span> 919-555-0187</p>
      <p><span class="contact__label">E:</span> darren@kestonlegalgroup.com</p>
      <p class="contact__web">www.kestonlegalgroup.com</p>
    </div>
  </section>

  <section class="card card--back" aria-label="Business card, blue side">
    <div class="firm-mark"><span class="firm-mark__dot"></span><span>Keston Legal</span></div>
    <p class="practice-areas">Personal Injury<span class="sep">|</span>Criminal Law</p>
    <p class="credentials">Former Insurance Company Attorney<span class="sep">|</span>Former Criminal Prosecutor</p>
  </section>

</body>
</html>
```